Crypto Exchange Comparison Platform

Let’s design a page that lets users compare hundreds of cryptocurrency exchanges. It will help users compare more info than anywhere else so you can find the best crypto exchange for your needs. The goal is to transform complex data into a clean, visually engaging experience.

Key Features to Design:
- Interactive comparison table with ~ 30 columns
- Filters and dropdown menus for easier usability
- Summary boxes for quick-view statistics
- Visual charts and graphs for key metrics
- Web, mobile, and tablet responsive design

Design Goals:
- Clean, modern aesthetic that makes complex data easily digestible
- Interactive elements (eg. Bar and Spider charts) for user engagement
- "Screenshot-friendly" sections for social media and sharing
- Data visualization focus (charts, graphs, metrics)
- Extremely easy to use on mobile
- Designs that use the color green
- A brand that communicates research and trusted information

Deliverables:
- High-fidelity mockup for desktop, tablet, and mobile versions
- Interactive prototype (Figma preferred)
- Style guide (typography, colors, components)

Note: The goal is to create an intuitive, visually engaging tool that helps users compare cryptocurrency exchanges efficiently while maintaining a clean, professional appearance that works well for social media sharing and content creation.
Updates

Low design quality

Industry/Entity Type

FinTech, Crypto, Finance

Number of Pages Required

1 page

Font styles to use
Other font styles liked:
• Inter or something good for a finance/data related website site

Colors
00AB8E
00BBA5
67D7C9
C6EFE9
E9F9F6

Requirements
Must have
• Please refer to the sketch I uploaded

```html
<!DOCTYPE html>
<html lang="en">
<head>
<meta charset="utf-8">
<title>Crypto Exchange Comparison</title>
<link href="https://fonts.googleapis.com/css2?family=Barlow:wght@400;500;600;700&family=Outfit:wght@400;500&display=swap" rel="stylesheet">
<style>
:root{
  --green-900:#00AB8E;
  --green-700:#00BBA5;
  --green-400:#67D7C9;
  --green-200:#C6EFE9;
  --green-100:#E9F9F6;
  --ink:#111;
  --black:#000;
  --bar:#2b2b2b;
  --card-dark:#101010;
  --muted:#555;
  --cell-a:#f4f4f4;
  --cell-b:#e6e6e6;
  --white:#fff;
  --yellow:#fcc419;
  --red:#ef5350;
  --cyan:#5ec8d4;
}
*{box-sizing:border-box;margin:0;padding:0}
html,body{width:1200px;height:2921px;overflow:hidden}
body{font-family:'Barlow',sans-serif;color:var(--ink);background:var(--white);position:relative}
a{color:var(--green-900)}
.abs{position:absolute}

/* header */
.site-header{position:absolute;left:0;top:0;width:1200px;height:96px;background:var(--black);border-top:2px solid var(--green-700);display:flex;align-items:center;justify-content:center}
.site-title{font-family:'Outfit',sans-serif;font-weight:400;color:var(--white);font-size:31px;letter-spacing:.3px}
.stat-strip{position:absolute;left:0;top:96px;width:1200px;height:59px;background:var(--bar);display:flex;align-items:center;justify-content:center;gap:62px;color:var(--white);font-weight:600;font-size:16px}
.stat-strip .item{display:flex;align-items:center;gap:18px}
.strip-icon{width:30px;height:30px;border-radius:50%;background:#1f4a43;display:flex;align-items:center;justify-content:center}

/* hero */
.hero{position:absolute;left:0;top:155px;width:1200px;height:602px;background:
 radial-gradient(ellipse 700px 120px at 780px 250px,rgba(0,171,142,.35),transparent 70%),
 radial-gradient(ellipse 600px 90px at 350px 330px,rgba(0,171,142,.25),transparent 70%),
 linear-gradient(160deg,#000 0%,#041410 45%,#000 100%)}
.section-heading{font-family:'Barlow',sans-serif;font-weight:500;color:var(--white);font-size:24px}
.disclosure{position:absolute;right:111px;top:46px;font-size:12px;color:var(--green-700)}
.pick-card{position:absolute;top:83px;width:314px;height:132px;background:var(--card-dark);border-radius:14px;padding:22px 20px 0 88px;color:var(--white)}
.pick-card .coin{position:absolute;left:22px;top:28px;width:46px;height:46px;border-radius:50%}
.pick-card h3{font-size:15px;font-weight:600;margin-bottom:8px}
.pick-card p{font-size:12px;line-height:21px;font-weight:500}
.pick-card a{display:block;margin-top:6px;font-size:10px}
.pick-card .go{position:absolute;right:0;bottom:0;width:34px;height:34px;border-radius:14px 0 14px 0;background:#1c1c1c;display:flex;align-items:center;justify-content:center}

/* table panel */
.table-panel{position:absolute;left:111px;top:425px;width:977px;height:628px;background:var(--white);border-radius:24px;box-shadow:0 6px 30px rgba(0,0,0,.1)}
.tabs{position:absolute;left:32px;top:30px;display:flex;gap:12px}
.tab{height:36px;padding:0 22px;border-radius:18px;background:var(--white);box-shadow:0 2px 8px rgba(0,0,0,.12);font-size:15px;font-weight:500;color:#444;display:flex;align-items:center}
.tab.active{background:var(--green-700);color:var(--white);padding:0 31px}
.select-pill{position:absolute;right:32px;top:30px;height:36px;width:118px;border-radius:18px;box-shadow:0 2px 8px rgba(0,0,0,.12);display:flex;align-items:center;justify-content:space-between;padding:0 14px 0 16px;font-size:15px;color:#444;font-weight:500}
.compare-table{position:absolute;left:32px;top:91px;width:915px;border-collapse:collapse;border-radius:18px;overflow:hidden}
.compare-table th{height:78px;font-weight:500;font-size:15px;line-height:19px;text-align:center;background:var(--cell-a);color:var(--ink)}
.compare-table td{height:100px;font-size:12.5px;text-align:center;color:#444;border-top:1px solid #dcdcdc}
.compare-table th:first-child,.compare-table td:first-child{width:126px;text-align:left;padding-left:19px;background:var(--white)}
.compare-table .shade{background:var(--cell-b)!important}
.compare-table td:not(:first-child):not(.shade),.compare-table th:not(:first-child):not(.shade){background:var(--cell-a)}
.exchange{display:flex;flex-direction:column;gap:10px;font-size:12px}
.exchange .mark{width:28px;height:28px;border-radius:50%}
.compare-table td a{font-size:12.5px}
.pager{position:absolute;right:30px;top:590px;display:flex;align-items:center;gap:10px;font-size:14px;font-weight:600}
.pager .btn{width:22px;height:22px;border-radius:50%;display:flex;align-items:center;justify-content:center}

/* charts */
.dropdown{position:absolute;height:43px;border-radius:22px;background:var(--green-900);color:var(--white);font-weight:600;font-size:15px;display:flex;align-items:center;justify-content:space-between;padding:0 20px 0 26px}
.chart-card{position:absolute;top:1173px;width:468px;height:230px;background:var(--white);border-radius:22px;box-shadow:0 4px 24px rgba(0,0,0,.1)}
.axis{font-family:'Barlow',sans-serif;font-size:4.5px;fill:#444}

/* stats */
.stat-box{position:absolute;top:1465px;width:229px;height:105px;background:linear-gradient(135deg,var(--green-900),var(--green-700));border-radius:6px;color:var(--white);padding:14px 16px;box-shadow:0 3px 10px rgba(0,0,0,.15)}
.stat-box .num{font-size:32px;font-weight:700;line-height:40px}
.stat-box .lbl{font-size:15px;font-weight:600;margin-top:4px}
.stat-box .ico{position:absolute;right:16px;top:24px;width:58px;height:58px;border-radius:50%;background:var(--white);display:flex;align-items:center;justify-content:center}

/* compare */
.compare-section{position:absolute;left:0;top:1640px;width:1200px;height:748px;background:linear-gradient(180deg,#000,#020605 60%,#000)}
.compare-title{position:absolute;left:111px;top:50px;font-family:'Outfit',sans-serif;font-weight:400;font-size:32px;color:var(--white)}
.radar-card{position:absolute;left:112px;top:116px;width:495px;height:277px;border-radius:24px;background:linear-gradient(180deg,#3a3a3a,#232323);overflow:hidden}
.score-card{position:absolute;left:113px;top:426px;width:374px;height:257px;border-radius:24px;background:#121212}
.score-card table{position:absolute;left:37px;top:22px;border-collapse:collapse}
.score-card th{font-weight:500;font-size:15px;color:var(--green-700);height:32px;text-align:left}
.score-card td{font-size:15px;height:38px;color:var(--white);letter-spacing:1px}
.score-card td.k{color:var(--green-700);width:125px;letter-spacing:0}
.score-card td.b{width:116px}
.feature-panel{position:absolute;left:682px;top:153px;width:406px;color:var(--white)}
.feature-head{display:flex;justify-content:space-between;align-items:center;height:30px}
.feature-head span{color:var(--green-700);font-weight:600;font-size:17px;text-decoration:underline}
.feature-row{display:grid;grid-template-columns:200px 146px 60px;height:54px;align-items:center;border-bottom:1px solid #333;font-size:15px;font-weight:500}
.feature-row:last-child{border-bottom:none}
.feature-row .v{text-align:center}
.collapse-row{display:flex;justify-content:space-between;align-items:center;height:42px;font-weight:700;font-size:16px;letter-spacing:.3px}
.cta{position:absolute;left:682px;top:638px;width:406px;height:48px;border-radius:24px;background:var(--green-900);border:1px solid var(--green-400);color:var(--white);font-weight:600;font-size:16px;display:flex;align-items:center;justify-content:center}

/* faq */
.faq-title{position:absolute;left:0;top:2454px;width:1200px;text-align:center;font-family:'Outfit',sans-serif;font-weight:400;font-size:32px}
.faq-item{position:absolute;left:216px;width:769px;height:62px;border-radius:31px;background:var(--white);box-shadow:0 3px 14px rgba(0,0,0,.1);display:flex;align-items:center;justify-content:space-between;padding:0 32px 0 34px;font-size:18px;color:#444;letter-spacing:.3px}

/* footer */
.site-footer{position:absolute;left:0;top:2870px;width:1200px;height:51px;background:var(--green-900);color:var(--white);display:flex;align-items:center;justify-content:space-between;padding:0 111px;font-size:15px;font-weight:600}
.socials{display:flex;gap:9px}
.socials span{width:27px;height:27px;border-radius:50%;background:var(--white)}
</style>
</head>
<body>

<header class="site-header"><h1 class="site-title">Crypto Exchange Comparison</h1></header>
<div class="stat-strip">
  <div class="item"><span class="strip-icon"><svg width="14" height="14" viewBox="0 0 14 14"><circle cx="5" cy="7" r="3" fill="none" stroke="#00BBA5" stroke-width="2"/><circle cx="10" cy="5" r="2" fill="#00BBA5"/></svg></span>Platforms Tracked: 125</div>
  <div class="item"><span class="strip-icon"><svg width="14" height="14" viewBox="0 0 14 14"><circle cx="7" cy="7" r="5" fill="none" stroke="#00BBA5" stroke-width="2" stroke-dasharray="2 2"/></svg></span>Updated: Feb 16,2025</div>
  <div class="item"><span class="strip-icon"><svg width="14" height="14" viewBox="0 0 14 14"><path d="M2 12 L12 2 L9 12 L7 8 Z" fill="#00BBA5"/></svg></span>How We Test &gt;</div>
</div>

<section class="hero">
  <h2 class="section-heading abs" style="left:111px;top:35px">Top Picks</h2>
  <a class="disclosure" href="#">Affiliate Disclosure</a>
  <article class="pick-card" style="left:111px">
    <span class="coin" style="background:#f7931a"></span>
    <h3>VAULTCOIN</h3>
    <p>Quis autem vel eum iure reprehen der<br>it qui in ea voluptate vel</p>
    <a href="#">WWW.VAULTCOIN.EXAMPLE</a>
    <span class="go"><svg width="10" height="10" viewBox="0 0 10 10"><path d="M1 5h6M5 2l3 3-3 3" stroke="#00BBA5" stroke-width="2" fill="none"/></svg></span>
  </article>
  <article class="pick-card" style="left:442px">
    <span class="coin" style="background:#f2f2f2"></span>
    <h3>LUMORA</h3>
    <p>Quis autem vel eum iure reprehen der<br>it qui in ea voluptate vel</p>
    <a href="#">WWW.LUMORA.EXAMPLE</a>
    <span class="go"><svg width="10" height="10" viewBox="0 0 10 10"><path d="M1 5h6M5 2l3 3-3 3" stroke="#00BBA5" stroke-width="2" fill="none"/></svg></span>
  </article>
  <article class="pick-card" style="left:773px">
    <span class="coin" style="background:#26a17b"></span>
    <h3>ANCHORLINE</h3>
    <p>Quis autem vel eum iure reprehen der<br>it qui in ea voluptate vel</p>
    <a href="#">WWW.ANCHORLINE.EXAMPLE</a>
    <span class="go"><svg width="10" height="10" viewBox="0 0 10 10"><path d="M1 5h6M5 2l3 3-3 3" stroke="#00BBA5" stroke-width="2" fill="none"/></svg></span>
  </article>
</section>

<section class="table-panel">
  <div class="tabs"><span class="tab active">Fees</span><span class="tab">Features</span><span class="tab">Security</span></div>
  <div class="select-pill">Compare <svg width="8" height="12" viewBox="0 0 8 12"><path d="M1 5l3-4 3 4zM1 7l3 4 3-4z" fill="#444"/></svg></div>
  <table class="compare-table">
    <thead><tr>
      <th>Logo &amp; Name</th><th class="shade">Last<br>Updated</th><th>Maker Fee</th><th class="shade">Taker Fee</th><th>Futures<br>Maker Fee</th><th class="shade">Futures<br>Taker Fee</th><th>Trading Fee<br>Discounts</th><th class="shade">Discount Or<br>Bonus</th><th>Visit</th>
    </tr></thead>
    <tbody>
      <tr><td><div class="exchange"><span class="mark" style="background:#f3ba2f"></span>Kestrel Coin</div></td><td class="shade">02/17/2025</td><td>0.10%</td><td class="shade">0.20%</td><td>0.50%</td><td class="shade">0.70%</td><td>Yes</td><td class="shade">$1,000</td><td><a href="#">kestrel</a></td></tr>
      <tr><td><div class="exchange"><span class="mark" style="background:#111"></span>Solvane</div></td><td class="shade">02/17/2025</td><td>0.10%</td><td class="shade">0.20%</td><td>0.50%</td><td class="shade">0.70%</td><td>Yes</td><td class="shade">$1,000</td><td><a href="#">Solvane</a></td></tr>
      <tr><td><div class="exchange"><span class="mark" style="background:#2a4fa8;width:22px;height:22px"></span>Meridano</div></td><td class="shade">02/17/2025</td><td>0.10%</td><td class="shade">0.20%</td><td>0.50%</td><td class="shade">0.70%</td><td>Yes</td><td class="shade">$1,000</td><td><a href="#">Meridano</a></td></tr>
      <tr><td><div class="exchange"><span class="mark" style="background:#2775ca"></span>Dollar Token</div></td><td class="shade">02/17/2025</td><td>0.10%</td><td class="shade">0.20%</td><td>0.50%</td><td class="shade">0.70%</td><td>Yes</td><td class="shade">$1,000</td><td><a href="#">Dollar Token</a></td></tr>
    </tbody>
  </table>
  <nav class="pager">
    <span class="btn" style="background:var(--green-900)"><svg width="8" height="8" viewBox="0 0 8 8"><path d="M5 1L2 4l3 3" stroke="#fff" stroke-width="2" fill="none"/></svg></span>
    <span><span style="color:var(--green-900)">1</span>, 2, 3 ... 9</span>
    <span class="btn" style="background:var(--green-200)"><svg width="8" height="8" viewBox="0 0 8 8"><path d="M3 1l3 3-3 3" stroke="#fff" stroke-width="2" fill="none"/></svg></span>
  </nav>
</section>

<div class="dropdown" style="left:111px;top:1106px;width:154px">Maker Fees <svg width="8" height="12" viewBox="0 0 8 12"><path d="M1 5l3-4 3 4zM1 7l3 4 3-4z" fill="#fff"/></svg></div>
<div class="dropdown" style="left:620px;top:1106px;width:171px">Trading Volume <svg width="8" height="12" viewBox="0 0 8 12"><path d="M1 5l3-4 3 4zM1 7l3 4 3-4z" fill="#fff"/></svg></div>

<div class="chart-card" style="left:111px">
  <svg width="468" height="230" viewBox="0 0 468 230">
    <g stroke="#e2e2e2" stroke-width=".6">
      <line x1="40" y1="70" x2="436" y2="70"/><line x1="40" y1="83" x2="436" y2="83"/><line x1="40" y1="96" x2="436" y2="96"/><line x1="40" y1="109" x2="436" y2="109"/><line x1="40" y1="122" x2="436" y2="122"/><line x1="40" y1="135" x2="436" y2="135"/><line x1="40" y1="148" x2="436" y2="148"/><line x1="40" y1="161" x2="436" y2="161"/><line x1="40" y1="174" x2="436" y2="174"/><line x1="40" y1="187" x2="436" y2="187"/><line x1="40" y1="200" x2="436" y2="200"/>
      <line x1="43" y1="70" x2="43" y2="200"/><line x1="76" y1="70" x2="76" y2="200"/><line x1="109" y1="70" x2="109" y2="200"/><line x1="142" y1="70" x2="142" y2="200"/><line x1="175" y1="70" x2="175" y2="200"/><line x1="208" y1="70" x2="208" y2="200"/><line x1="241" y1="70" x2="241" y2="200"/><line x1="274" y1="70" x2="274" y2="200"/><line x1="307" y1="70" x2="307" y2="200"/><line x1="340" y1="70" x2="340" y2="200"/><line x1="373" y1="70" x2="373" y2="200"/><line x1="406" y1="70" x2="406" y2="200"/><line x1="436" y1="70" x2="436" y2="200"/>
    </g>
    <g class="axis" text-anchor="end"><text x="37" y="72">100</text><text x="37" y="98">80</text><text x="37" y="124">60</text><text x="37" y="150">40</text><text x="37" y="176">20</text><text x="37" y="202">0</text></g>
    <g fill="var(--yellow)"><rect x="50" y="187" width="20" height="13"/><rect x="83" y="161" width="20" height="39"/><rect x="116" y="184" width="20" height="16"/><rect x="149" y="179" width="20" height="21"/><rect x="182" y="148" width="20" height="52"/><rect x="215" y="184" width="20" height="16"/><rect x="248" y="166" width="20" height="34"/><rect x="281" y="174" width="20" height="26"/><rect x="314" y="184" width="20" height="16"/><rect x="347" y="156" width="20" height="44"/><rect x="380" y="166" width="20" height="34"/><rect x="413" y="184" width="20" height="16"/></g>
    <g fill="var(--red)"><rect x="50" y="174" width="20" height="13"/><rect x="83" y="122" width="20" height="39"/><rect x="116" y="166" width="20" height="18"/><rect x="149" y="93" width="20" height="86"/><rect x="182" y="122" width="20" height="26"/><rect x="215" y="166" width="20" height="18"/><rect x="248" y="140" width="20" height="26"/><rect x="281" y="148" width="20" height="26"/><rect x="314" y="166" width="20" height="18"/><rect x="347" y="109" width="20" height="47"/><rect x="380" y="132" width="20" height="34"/><rect x="413" y="166" width="20" height="18"/></g>
    <g fill="var(--cyan)"><rect x="50" y="161" width="20" height="13"/><rect x="83" y="83" width="20" height="39"/><rect x="116" y="122" width="20" height="44"/><rect x="149" y="70" width="20" height="23"/><rect x="182" y="96" width="20" height="26"/><rect x="248" y="106" width="20" height="34"/><rect x="281" y="88" width="20" height="60"/><rect x="314" y="135" width="20" height="31"/><rect x="380" y="106" width="20" height="26"/><rect x="413" y="150" width="20" height="16"/></g>
    <g class="axis" text-anchor="middle"><text x="60" y="212">JAN</text><text x="93" y="212">FEB</text><text x="126" y="212">MAR</text><text x="159" y="212">APR</text><text x="192" y="212">MAY</text><text x="225" y="212">JUN</text><text x="258" y="212">JUL</text><text x="291" y="212">AUG</text><text x="324" y="212">SEP</text><text x="357" y="212">OCT</text><text x="390" y="212">NOV</text><text x="423" y="212">DEC</text></g>
  </svg>
</div>

<div class="chart-card" style="left:620px">
  <svg width="468" height="230" viewBox="0 0 468 230">
    <g stroke="#e2e2e2" stroke-width=".6">
      <line x1="30" y1="45" x2="440" y2="45"/><line x1="30" y1="58" x2="440" y2="58"/><line x1="30" y1="72" x2="440" y2="72"/><line x1="30" y1="86" x2="440" y2="86"/><line x1="30" y1="100" x2="440" y2="100"/><line x1="30" y1="114" x2="440" y2="114"/><line x1="30" y1="128" x2="440" y2="128"/><line x1="30" y1="142" x2="440" y2="142"/><line x1="30" y1="156" x2="440" y2="156"/><line x1="30" y1="170" x2="440" y2="170"/>
      <line x1="35" y1="45" x2="35" y2="170"/><line x1="71" y1="45" x2="71" y2="170"/><line x1="108" y1="45" x2="108" y2="170"/><line x1="144" y1="45" x2="144" y2="170"/><line x1="180" y1="45" x2="180" y2="170"/><line x1="217" y1="45" x2="217" y2="170"/><line x1="253" y1="45" x2="253" y2="170"/><line x1="290" y1="45" x2="290" y2="170"/><line x1="326" y1="45" x2="326" y2="170"/><line x1="362" y1="45" x2="362" y2="170"/><line x1="399" y1="45" x2="399" y2="170"/><line x1="435" y1="45" x2="435" y2="170"/>
    </g>
    <g class="axis" text-anchor="end"><text x="28" y="47">100</text><text x="28" y="74">80</text><text x="28" y="102">60</text><text x="28" y="130">40</text><text x="28" y="158">20</text><text x="28" y="172">0</text></g>
    <polyline fill="none" stroke="#a5cd39" stroke-width="1.2" points="35,122 71,110 108,122 144,84 180,84 217,98 253,84 290,84 326,64 362,60 399,60 435,64"/>
    <g fill="#a5cd39"><circle cx="35" cy="122" r="1.8"/><circle cx="71" cy="110" r="1.8"/><circle cx="108" cy="122" r="1.8"/><circle cx="144" cy="84" r="1.8"/><circle cx="180" cy="84" r="1.8"/><circle cx="217" cy="98" r="1.8"/><circle cx="253" cy="84" r="1.8"/><circle cx="290" cy="84" r="1.8"/><circle cx="326" cy="64" r="1.8"/><circle cx="362" cy="60" r="1.8"/><circle cx="399" cy="60" r="1.8"/><circle cx="435" cy="64" r="1.8"/></g>
    <polyline fill="none" stroke="#e6427a" stroke-width="1.2" points="35,158 71,134 108,152 144,116 180,104 217,122 253,110 290,122 326,96 362,68 399,84 435,68"/>
    <g fill="#e6427a"><circle cx="35" cy="158" r="1.8"/><circle cx="71" cy="134" r="1.8"/><circle cx="108" cy="152" r="1.8"/><circle cx="144" cy="116" r="1.8"/><circle cx="180" cy="104" r="1.8"/><circle cx="217" cy="122" r="1.8"/><circle cx="253" cy="110" r="1.8"/><circle cx="290" cy="122" r="1.8"/><circle cx="326" cy="96" r="1.8"/><circle cx="362" cy="68" r="1.8"/><circle cx="399" cy="84" r="1.8"/><circle cx="435" cy="68" r="1.8"/></g>
    <g class="axis" text-anchor="middle"><text x="53" y="190">JAN</text><text x="89" y="190">FEB</text><text x="126" y="190">MAR</text><text x="162" y="190">APR</text><text x="198" y="190">MAY</text><text x="235" y="190">JUN</text><text x="271" y="190">JUL</text><text x="308" y="190">AUG</text><text x="344" y="190">SEP</text><text x="380" y="190">OCT</text><text x="417" y="190">NOV</text><text x="452" y="190">DEC</text></g>
  </svg>
</div>

<div class="stat-box" style="left:113px"><div class="num">125</div><div class="lbl">Exchanges Tracked</div>
  <span class="ico"><svg width="30" height="26" viewBox="0 0 30 26"><g fill="#111"><rect x="3" y="14" width="4" height="11"/><rect x="10" y="10" width="4" height="15"/><rect x="17" y="13" width="4" height="12"/><rect x="24" y="6" width="4" height="19"/></g><polyline points="3,10 11,5 18,9 27,1" fill="none" stroke="#111" stroke-width="2"/></svg></span></div>
<div class="stat-box" style="left:361px"><div class="num">0.15%</div><div class="lbl">Average Trading Fee</div>
  <span class="ico"><svg width="30" height="26" viewBox="0 0 30 26"><g fill="#111"><rect x="3" y="10" width="5" height="12"/><rect x="11" y="6" width="5" height="12"/><rect x="19" y="12" width="5" height="10"/><rect x="26" y="4" width="3" height="14"/></g><g stroke="#111" stroke-width="1.5"><line x1="5.5" y1="6" x2="5.5" y2="25"/><line x1="13.5" y1="2" x2="13.5" y2="21"/><line x1="21.5" y1="8" x2="21.5" y2="25"/></g></svg></span></div>
<div class="stat-box" style="left:609px"><div class="num">892M</div><div class="lbl">Total Users</div>
  <span class="ico"><svg width="32" height="26" viewBox="0 0 32 26"><g fill="#111"><circle cx="16" cy="7" r="5"/><circle cx="7" cy="10" r="3.5"/><circle cx="25" cy="10" r="3.5"/><path d="M8 25a8 8 0 0 1 16 0z"/><path d="M0 24a7 6 0 0 1 9-6v6z"/><path d="M32 24a7 6 0 0 0-9-6v6z"/></g></svg></span></div>
<div class="stat-box" style="left:858px"><div class="num">12.2B</div><div class="lbl">Web Visitors (30D)</div>
  <span class="ico"><svg width="30" height="30" viewBox="0 0 30 30"><circle cx="14" cy="14" r="12" fill="#111"/><g stroke="#fff" stroke-width="1.2" fill="none"><ellipse cx="14" cy="14" rx="5" ry="12"/><line x1="2" y1="14" x2="26" y2="14"/></g><circle cx="22" cy="22" r="6.5" fill="#111" stroke="#fff" stroke-width="1.5"/></svg></span></div>

<section class="compare-section">
  <h2 class="compare-title">Compare</h2>
  <div class="radar-card">
    <svg width="495" height="277" viewBox="0 0 495 277">
      <defs>
        <linearGradient id="radarA" x1="0" y1="0" x2="1" y2="1"><stop offset="0" stop-color="#c36df0"/><stop offset="1" stop-color="#7a2fd0"/></linearGradient>
        <linearGradient id="radarB" x1="0" y1="0" x2="1" y2="1"><stop offset="0" stop-color="#bff4ff"/><stop offset="1" stop-color="#4fc5de"/></linearGradient>
      </defs>
      <g fill="none" stroke="#5a5a5a" stroke-width="1">
        <polygon points="190,30 320,30 385,138 320,246 190,246 125,138"/>
        <polygon points="207,58 303,58 352,138 303,218 207,218 158,138"/>
        <polygon points="223,86 287,86 319,138 287,190 223,190 191,138"/>
        <line x1="190" y1="30" x2="320" y2="246"/><line x1="320" y1="30" x2="190" y2="246"/><line x1="125" y1="138" x2="385" y2="138"/>
      </g>
      <polygon points="200,45 300,75 358,140 285,205 215,210 175,150" fill="url(#radarA)" opacity=".95"/>
      <polygon points="215,70 280,85 300,150 268,205 205,210 180,150" fill="url(#radarB)" opacity=".95"/>
      <g fill="#ddd"><circle cx="190" cy="30" r="2"/><circle cx="320" cy="30" r="2"/><circle cx="385" cy="138" r="2"/><circle cx="320" cy="246" r="2"/><circle cx="190" cy="246" r="2"/><circle cx="125" cy="138" r="2"/></g>
      <g font-family="Barlow, sans-serif" font-size="6" fill="#aaa"><text x="145" y="22">Adipiscing elit</text><text x="328" y="22">Phasellus</text><text x="392" y="141">Dolor sit</text><text x="328" y="260">Condimentum</text><text x="150" y="260">Lorem ipsum</text><text x="95" y="141">Iaculis amet</text></g>
    </svg>
  </div>
  <div class="score-card">
    <table>
      <tr><th></th><th>Kestrel</th><th>Harbor</th></tr>
      <tr><td class="k">Fees</td><td class="b">9/10</td><td>4/10</td></tr>
      <tr><td class="k">Security</td><td class="b">9/10</td><td>4/10</td></tr>
      <tr><td class="k">Features</td><td class="b">9/10</td><td>4/10</td></tr>
      <tr><td class="k">Deposits</td><td class="b">9/10</td><td>4/10</td></tr>
      <tr><td class="k">Withdrawals</td><td class="b">9/10</td><td>4/10</td></tr>
    </table>
  </div>
  <div class="dropdown" style="left:682px;top:73px;width:160px;background:var(--green-700);font-size:15px;padding:0 16px">Kestrel <svg width="8" height="12" viewBox="0 0 8 12"><path d="M1 5l3-4 3 4zM1 7l3 4 3-4z" fill="#fff"/></svg></div>
  <div class="dropdown" style="left:864px;top:73px;width:160px;background:var(--green-700);font-size:15px;padding:0 16px">Harbor <svg width="8" height="12" viewBox="0 0 8 12"><path d="M1 5l3-4 3 4zM1 7l3 4 3-4z" fill="#fff"/></svg></div>
  <div class="feature-panel">
    <div class="feature-head"><span>FEATURES</span><svg width="14" height="9" viewBox="0 0 14 9"><path d="M1 8l6-6 6 6" stroke="var(--green-700)" stroke-width="2.5" fill="none"/></svg></div>
    <div class="feature-row"><span># of Coins</span><span class="v">XYZ</span><span class="v">XYZ</span></div>
    <div class="feature-row"><span># of Futures</span><span class="v">XYZ</span><span class="v">XYZ</span></div>
    <div class="feature-row"><span>Trading Bots</span><span class="v">XYZ</span><span class="v">XYZ</span></div>
    <div class="feature-row"><span>Copy Trading</span><span class="v">XYZ</span><span class="v">XYZ</span></div>
    <div class="feature-row"><span>24/7 Support</span><span class="v">XYZ</span><span class="v">XYZ</span></div>
    <div class="collapse-row" style="margin-top:4px">SECURITY<svg width="14" height="9" viewBox="0 0 14 9"><path d="M1 1l6 6 6-6" stroke="#fff" stroke-width="2.5" fill="none"/></svg></div>
    <div class="collapse-row">FEES<svg width="14" height="9" viewBox="0 0 14 9"><path d="M1 1l6 6 6-6" stroke="#fff" stroke-width="2.5" fill="none"/></svg></div>
    <div class="collapse-row">DEPOSITS<svg width="14" height="9" viewBox="0 0 14 9"><path d="M1 1l6 6 6-6" stroke="#fff" stroke-width="2.5" fill="none"/></svg></div>
    <div class="collapse-row">WITHDRAWALS<svg width="14" height="9" viewBox="0 0 14 9"><path d="M1 1l6 6 6-6" stroke="#fff" stroke-width="2.5" fill="none"/></svg></div>
  </div>
  <div class="cta">Full Comparison</div>
</section>

<h2 class="faq-title">Frequently Asked Questions</h2>
<div class="faq-item" style="top:2520px">What are crypto exchanges?<svg width="16" height="16" viewBox="0 0 16 16"><circle cx="8" cy="8" r="7.5" fill="#444"/><path d="M8 4v8M4 8h8" stroke="#fff" stroke-width="2"/></svg></div>
<div class="faq-item" style="top:2598px">How to choose a crypto exchanges?<svg width="16" height="16" viewBox="0 0 16 16"><circle cx="8" cy="8" r="7.5" fill="#444"/><path d="M8 4v8M4 8h8" stroke="#fff" stroke-width="2"/></svg></div>
<div class="faq-item" style="top:2675px">How is this data tracked?<svg width="16" height="16" viewBox="0 0 16 16"><circle cx="8" cy="8" r="7.5" fill="#444"/><path d="M8 4v8M4 8h8" stroke="#fff" stroke-width="2"/></svg></div>
<div class="faq-item" style="top:2753px">How often is this page updated?<svg width="16" height="16" viewBox="0 0 16 16"><circle cx="8" cy="8" r="7.5" fill="#444"/><path d="M8 4v8M4 8h8" stroke="#fff" stroke-width="2"/></svg></div>

<footer class="site-footer">
  <span>(C) Copyright | All Rights Reserved</span>
  <div class="socials"><span></span><span></span><span></span><span></span></div>
</footer>

</body>
</html>
```